Bluecrest Ore Company needs a company newsletter template

We need a 2-page editable newsletter template, that we can update monthly with various information and pictures. We would like an area to include our values: Be Safe, Be Honest, Be Responsible, Be Respectful, Be Great. Ideally we would have 2-3 bulk text areas to highlight different things each month, with area we an update a picture from time to time and maybe some text areas where we can add a fun fact type thing. Some of the areas we will include are production milestones (if any), monthly tenure, monthly new hires, highlighting an employee that demonstrates our value, community engagement, upcoming holidays/events, press releases. The exact content will likely change month to month but these will be some of the frequent topics. We are a copper Mine in northern Yukon. I've attached our Brand Guidelines and logo files. Our website is ravelorex.com if you want to see the style and type of photos from our site

```html
<!DOCTYPE html>
<html lang="en">
<head>
<meta charset="utf-8">
<title>Bluecrest Ore Company – Monthly Newsletter</title>
<link rel="stylesheet" href="https://fonts.googleapis.com/css2?family=Montserrat:ital,wght@0,300;0,400;0,500;0,600;0,800;0,900&family=Tinos:ital@1&display=swap">
<style>
  :root {
    --rust: #8a382c;
    --rust-deep: #7a3025;
    --gold: #efbe2c;
    --navy: #22303f;
    --ink: #2b2b2b;
    --paper: #ffffff;
    --backdrop: #f2f0ec;
    --sky-top: #7aa6d6;
    --sky-low: #d8e3ee;
    --ground: #7a6a58;
  }
  * { box-sizing: border-box; margin: 0; padding: 0; }
  html, body { width: 1200px; height: 961px; overflow: hidden; }
  body { background: var(--backdrop); position: relative; font-family: "Montserrat", Arial, sans-serif; color: var(--ink); }

  .page { position: absolute; width: 449px; height: 581px; background: var(--paper); box-shadow: 0 8px 18px rgba(0,0,0,.18); overflow: hidden; }
  .page--front { left: 116px; top: 47px; }
  .page--back { left: 635px; top: 333px; width: 448px; height: 580px; }

  /* masthead */
  .masthead { position: absolute; left: 0; top: 0; width: 100%; height: 76px; background: var(--rust); }
  .brand { position: absolute; left: 0; top: 0; width: 125px; height: 76px; border-right: 1px solid var(--rust-deep); display: flex; flex-direction: column; align-items: center; justify-content: flex-end; padding-bottom: 11px; gap: 6px; }
  .brand__mark { width: 14px; height: 14px; background: var(--gold); }
  .brand__name { color: #fff; font-weight: 600; font-size: 9.6px; letter-spacing: .3px; white-space: nowrap; }
  .masthead__title { position: absolute; left: 134px; top: 11px; color: var(--gold); font-weight: 300; font-size: 42px; line-height: 1; letter-spacing: 1.2px; }
  .values-strip { position: absolute; left: 125px; top: 59px; right: 0; height: 17px; background: var(--gold); color: var(--rust-deep); font-size: 8.3px; line-height: 17px; padding-left: 11px; white-space: nowrap; }

  /* front page */
  .sidebar { position: absolute; left: 0; top: 76px; width: 125px; height: 505px; background: var(--navy); }
  .section-head { position: relative; font-weight: 800; font-size: 13.5px; line-height: 15px; padding-left: 20px; }
  .section-head::before { content: ""; position: absolute; left: 0; top: 3px; width: 11px; height: 11px; background: linear-gradient(135deg, var(--gold) 50%, var(--rust) 50%); }
  .section-head__lead { display: block; }
  .section-head__tail { display: block; color: var(--gold); }
  .sidebar .section-head { color: #fff; }
  .sidebar .section-head--hires { position: absolute; top: 19px; left: 0; }
  .sidebar .section-head--press { position: absolute; top: 273px; left: 0; }
  .hire-photo { position: absolute; left: 21px; top: 55px; width: 94px; height: 61px; background: linear-gradient(160deg, #8a8f96 0%, #4a4f55 55%, #d29a3a 100%); }
  .brief { font-family: "Tinos", "Times New Roman", serif; font-style: italic; font-size: 6.5px; line-height: 7.3px; color: #fff; }
  .brief p + p { margin-top: 7px; }
  .sidebar .brief { position: absolute; left: 21px; width: 90px; }
  .brief--hires { top: 132px; }
  .brief--press { top: 306px; }

  .feature-photo { position: absolute; left: 125px; top: 76px; width: 324px; height: 210px; background: linear-gradient(180deg, var(--sky-top) 0%, var(--sky-low) 55%, #a8a194 66%, var(--ground) 100%); }
  .feature-title { position: absolute; left: 143px; top: 94px; font-size: 21.5px; line-height: 22px; color: var(--ink); font-weight: 400; letter-spacing: .2px; }
  .feature-title strong { font-weight: 900; color: var(--rust); }

  .article { font-size: 7.1px; line-height: 9.9px; letter-spacing: -0.05px; }
  .article p + p { margin-top: 9px; }
  .drop-cap::first-letter { float: left; font-weight: 300; font-size: 31px; line-height: 26px; margin: 1px 4px 0 2px; color: var(--rust); }
  .article--feature { position: absolute; left: 143px; top: 303px; width: 286px; color: #333; }

  /* back page */
  .spread { position: absolute; left: 0; top: 75px; width: 100%; height: 246px; background: var(--rust); }
  .page--back .masthead { height: 75px; }
  .page--back .brand { height: 75px; width: 124px; }
  .page--back .values-strip { left: 124px; top: 60px; }
  .page--back .masthead__title { left: 135px; top: 12px; }
  .article--spread { position: absolute; top: 12px; width: 193px; color: #fff; font-size: 7.1px; line-height: 10.1px; }
  .article--spread.col-a { left: 20px; }
  .article--spread.col-b { left: 234px; }
  .article--spread .drop-cap::first-letter { color: #fff; }

  .topics { position: absolute; left: 6px; top: 330px; width: 436px; display: grid; grid-template-columns: repeat(3, 1fr); column-gap: 0; }
  .topic .section-head { color: var(--rust); padding-left: 14px; font-size: 13.3px; }
  .topic .section-head::before { top: 2px; }
  .topic .section-head__tail { color: var(--gold); }
  .topic .brief { color: #222; border-left: 1px solid var(--rust); margin: 0 0 0 2px; padding: 10px 10px 0 11px; height: 222px; font-size: 6.5px; line-height: 8.1px; overflow: hidden; }
  .topic .brief p + p { margin-top: 8px; }
</style>
</head>
<body>

<article class="page page--front">
  <header class="masthead">
    <div class="brand"><span class="brand__mark"></span><span class="brand__name">BLUECREST ORE</span></div>
    <h1 class="masthead__title">NEWSLETTER</h1>
    <p class="values-strip">BE SAFE, BE HONEST, BE RESPONSIBLE, BE RESPECTFUL, BE GREAT.</p>
  </header>

  <aside class="sidebar">
    <h2 class="section-head section-head--hires"><span class="section-head__lead">Monthly</span><span class="section-head__tail">New Hires</span></h2>
    <div class="hire-photo" role="img" aria-label="Photo of a new hire in hard hat and safety vest at the mine site"></div>
    <div class="brief brief--hires">
      <p>Lorem ipsum dolor sit amet, consectetur adipiscing elit. Duis risus libero, condim enim. Curabitur non condimentum diam. Morbi suscipit, risus non maximus semper, elit nisl placerat augue.</p>
      <p>Nulla id vehicula tellus. Duis vitae cons equat dolor. Fusce ultricies tortor ipsum, aam est.</p>
      <p>Nunc pretium libero hendrerit justo cons ectetur ornare. Etiam dictum metus id tu rpis volutpat, nec interdum ipsum phaas retra. tibulum molestie dignissim.</p>
    </div>

    <h2 class="section-head section-head--press"><span class="section-head__lead">Press</span><span class="section-head__tail">Releases</span></h2>
    <div class="brief brief--press">
      <p>Lorem ipsum dolor sit amet, consectetur adipiscing elit. Duis risus libero, condim enim. Curabitur non condimentum diam. Morbi suscipit, risus non maximus semper, elit nisl placerat augue.</p>
      <p>Nulla id vehicula tellus. Duis vitae cons equat dolor. Fusce ultricies tortor ipsum, a Nulla id vehicula tellus. Duis vitae cons equat dolor. Fusce ultricies tortor ipsum. Nulla id vehicula tellus. Duis vitae cons equat dolor. Fusce ultricies tortor ipsum nulla id vehicula tellus. Duis</p>
      <p>Nunc pretium libero hendrerit justo cons ectetur ornare. Etiam dictum metus id tu rpis volutpat, nec interdum us id tu rpis volutpat, nec interdum ipsum phaas retra. tibulum molestie dignissim.</p>
    </div>
  </aside>

  <div class="feature-photo" role="img" aria-label="Photo of a large yellow haul truck at an open-pit mine under a blue sky"></div>
  <h2 class="feature-title"><strong>TITTLE HERE</strong> AMET<br>LOREMIPSUM<br><strong>DOLORSIT</strong></h2>

  <div class="article article--feature">
    <p class="drop-cap">Lorem ipsum dolor sit amet, consectetur adipiscing elit. Duis risus libero, condimentum in molestie quis, gravida non justo. Integer aliquam tellus id nisl fringilla sollicitudin. Curabitur non condimentum diam. Morbi suscipit, risus non maximus semper, elit nisl placerat augue, id pharetra nulla neque ac diam. Curabitur eu malesuada nunc. Phasellus in aliquam lectus, et blandit enim. Mauris dignissim varius tortor, et tincidunt augue euismod sit amet. In hac habitasse platea dictumst. Praesent enim est, rutrum et velit quis, lobortis cursus dui. Praesent ultrices, mi in molestie efficitur, est urna scelerisque nunc, quis vestibulum eros risus vitae lectus.</p>
    <p>Nulla id vehicula tellus. Duis vitae consequat dolor. Fusce ultricies tortor ipsum, ac tempus mi iaculis et. Fusce quis fermentum enim. Curabitur tempus suscipit faucibus. Sed eu cursus orci, tincidunt tincidunt turpis. Vestibulum ante ipsum primis in faucibus orci luctus et ultrices posuere cubilia curae; Donec turpis turpis, pretium non elit quis, fermentum dignissim massa. Nam vitae odio non augue mattis malesuada. Etiam est diam, ullamcorper lacinia rhoncus quis, gravida venenatis magna.</p>
    <p>Nunc pretium libero hendrerit justo consectetur ornare. Etiam dictum metus id turpis volutpat, nec interdum ipsum pharetra. Sed et vestibulum dolor. Nam sapien nibh, dictum nec lacinia non, laoreet in nulla. Vestibulum molestie dignissim tristmpus suscipit faucibus. Sed eu cursus orci, tincidunt tincidunt turpis. Vestibulum ante ipsum primis in faucibus orci luctus et ultrices posuere cubilia curae; Donec tumpus suscipit faucibus. Sed eu cursus orci, tincidunt tincidunt turpis. Vestibulum ante ipsum primis in faucibus orci luctus et ultrices posuere cubilia curae; Donec tuique. Nulla pellentesque.</p>
  </div>
</article>

<article class="page page--back">
  <header class="masthead">
    <div class="brand"><span class="brand__mark"></span><span class="brand__name">BLUECREST ORE</span></div>
    <h1 class="masthead__title">NEWSLETTER</h1>
    <p class="values-strip">BE SAFE, BE HONEST, BE RESPONSIBLE, BE RESPECTFUL, BE GREAT.</p>
  </header>

  <section class="spread">
    <div class="article article--spread col-a">
      <p class="drop-cap">Lorem ipsum dolor sit amet, consectetur adipiscing elit. Duis risus libero, condi ment um in molestie quis, gravida non justo. Integ er aliquam tellus id nisl fringilla sollicitudin. Curabitur non condimentum diam. Morbi suscipit, risus non maximus semper, elit nisl placerat augue, id pharetra nulla neque ac diam. Curabitur eu malesuada nunc. Phasellus in aliquam lectus, et blandit enim. Mauris dignissim varius tortor, et tincidunt augue euismod sit amet. In hac habitasse platea dictumst. Praesent enim est, rutrum et velit quis, lobortis cursus dui.</p>
      <p>Nulla id vehicula tellus. Duis vitae consequat dolor. Fusce ultricies tortor ipsum, ac tempus mi iaculis et. Fusce quis fermentum enim. Curabitur tempus suscipit faucibus. Sed eu cursus orci, tincidunt tincidunt turpis. Vest fermentum enim. Curabitur tempus suscipit faucibus. Sed eu cursus orci, tincidunt tincidunt turpis. Vestibuluibulum ante ipsum primis in faucibus orci luctus et ultrices posuere cubilia curae; Donec turpis turpis, pretium</p>
    </div>
    <div class="article article--spread col-b">
      <p>non elit quis, fermentum dignissim massa. Nam vitae odio non augue mattis malesuada. Etiam est diam, ullamc orper lacinia rhoncus quis, gravida venenatis magna. Nunc pretium libero hendrerit justo consectetur ornare. Etiam dictum metus id turpis volutpat, nec interdum ipsum pharetra. Sed et vestibulum dolor. Nam sapien nibh, dictum nec lacinia non, laoreet in nulla. Vestibulum molestie dignissim tristique. Nulla pellentesque urna leo, nec malesuada diam elementum elementum. Proin eget ipsum ligula.</p>
      <p>Donec fringilla, turpis sed convallis vestibulum, nunc augue hendrerit enim, ac fermentum arcu lorem at lectus. Sed ultricies lobortis neque, a porta est pre ium id. Sed magna s massa. Sed in mauris ac ante cursus pul vinar. Aenean molestie congueem, laoreet vitae viverra ut, lacinia in massa. Sed in mauris ac ante cursus pul vinar. Aenean molestie congue erat, nec porttitor urna vel ultricies et. Nam auctor purus lorem, vitae pharetra mi dapibus non. Ut mollis neque vita.</p>
    </div>
  </section>

  <section class="topics">
    <div class="topic">
      <h2 class="section-head"><span class="section-head__lead">Production</span><span class="section-head__tail">Milestones</span></h2>
      <div class="brief">
        <p>Lorem ipsum dolor sit amet, consectetur adipiscing elit. Duis risus libero, condim enin. Curabitur non condimentum diam. Morbi suscipit, risus non maximussaffga semper, elit nisl placerat augue.</p>
        <p>Nulla id vehicula tellus. Duis vitae cons equequat dolor. Fusce ultricies tortor ipsu m, aam est diat dolor. Fusce ul tri cies tortor ipsu m, aam est diam, ul lam corper lacinia rhon cus quis, gravida venenatis</p>
        <p>Nunc pretium libero hendrerit justo cons ectelestie dignissim tristas ique. Nulla pellentesque urna leo, nema l esuada diam elementum elementum. Proin eget ipsum nec interdum ipsum phaas retra. tibulum molestie dignissim tristas ique. Nulla pellentesque urna leo, nema l esuada diam elementum elemen tum. Proin eget ipsum nec interdum ipsu m phaas retra. tibulum molestie dign iss im tristas ique. Nulla pellentesque urna</p>
      </div>
    </div>
    <div class="topic">
      <h2 class="section-head"><span class="section-head__lead">Community</span><span class="section-head__tail">Engagement</span></h2>
      <div class="brief">
        <p>Lorem ipsum dolor sit amet, consectetur adipiscing elit. Duis risus libero, condim enin. Curabitur non condimentum diam. Morbi suscipit, risus non maximussaffga semper, elit nisl placerat augue.</p>
        <p>Nulla id vehicula tellus. Duis vitae cons equequat dolor. Fusce ultricies tortor ipsu m, aam est diat dolor. Fusce ul tri cies tortor ipsu m, aam est diam, ul lam corper lacinia rhon cus quis, gravida venenatis</p>
        <p>Nunc pretium libero hendrerit justo cons ectelestie dignissim tristas ique. Nulla pellentesque urna leo, nema l esuada diam elementum elementum. Proin eget ipsum nec interdum ipsum phaas retra. tibulum molestie dignissim tristas ique. Nulla pellentesque urna leo, nema l esuada diam elementum elemen tum. Proin eget ipsum nec interdum ipsu m phaas retra. tibulum molestie dign iss im tristas ique. Nulla pellentesque urna</p>
      </div>
    </div>
    <div class="topic">
      <h2 class="section-head"><span class="section-head__lead">Upcoming</span><span class="section-head__tail">Holidays/events</span></h2>
      <div class="brief">
        <p>Lorem ipsum dolor sit amet, consectetur adipiscing elit. Duis risus libero, condim enin. Curabitur non condimentum diam. Morbi suscipit, risus non maximussaffga semper, elit nisl placerat augue.</p>
        <p>Nulla id vehicula tellus. Duis vitae cons equequat dolor. Fusce ultricies tortor ipsu m, aam est diat dolor. Fusce ul tri cies tortor ipsu m, aam est diam, ul lam corper lacinia rhon cus quis, gravida venenatis</p>
        <p>Nunc pretium libero hendrerit justo cons ectelestie dignissim tristas ique. Nulla pellentesque urna leo, nema l esuada diam elementum elementum. Proin eget ipsum nec interdum ipsum phaas retra. tibulum molestie dignissim tristas ique. Nulla pellentesque urna leo, nema l esuada diam elementum elemen tum. Proin eget ipsum nec interdum ipsu m phaas retra. tibulum molestie dign iss im tristas ique. Nulla pellentesque urna</p>
      </div>
    </div>
  </section>
</article>

</body>
</html>
```